App Design - Job Lantern Quokka

We require an App Design for our new App called 'Lantern Quokka'. This app is essentially an assistant to help Users prepare for job interviews, to help them get hired. <br/><br/>Users who download the App can view common Questions and Answers, save their favourite responses and also view common Interview Tips. <br/><br/>The vision for our App is for Users who are preparing for an interview (1 week before, 1 day before, even 1 hour before), are able to download, view and educate themselves on common questions and responses, and then be confident to land the job. <br/><br/>Our team has developed wireframes to help highlight what each screen should do and include. Please see attached document, which also highlights key requirements for the experience. Feel free to add/remove/edit what you see on these wireframes. Our preference is that you use Adobe XD please.<br/><br/>In terms of design guidelines, we want the experience to be simple, intuitive and 'memorable' to help Users to remember the questions/responses when they are in the interview. <br/><br/>The final design should communicate 'neat and clean professionalism'; we like the design of: marlo vane com au<br/><br/>Thank you for reading! Good luck !

Target Market(s)

Professional job seekers

Font styles to use
Sans Serif

Colors

Designer to choose colors to be used in the design.

Requirements
Must have
• Please see my PlanHive_UX file that I have uploaded
Nice to have
• Could you also please include some ideas on how we can incorporate Advertising into the app screens

```html
<!DOCTYPE html>
<html lang="en">
<head>
<meta charset="utf-8">
<title>Lantern Quokka – App Screens</title>
<link href="https://fonts.googleapis.com/css2?family=Poppins:ital,wght@0,400;0,500;0,600;0,700;1,600&display=swap" rel="stylesheet">
<style>
  :root{
    --canvas:#c8c8c8;
    --photo-top:#0d3458;
    --photo-mid:#1d4763;
    --photo-low:#3f5a2a;
    --photo-base:#2b3a14;
    --panel:rgba(21,98,176,0.88);
    --accent:#e8c800;
    --ink:#ffffff;
    --ink-dark:#1c2a3a;
  }
  *{box-sizing:border-box;margin:0;padding:0}
  html,body{width:755px;height:1200px;overflow:hidden;background:var(--canvas)}
  body{position:relative;font-family:'Poppins',sans-serif;color:var(--ink)}
  .screen{position:absolute;width:318px;overflow:hidden}
  .screen--splash{left:37px;top:30px;height:506px}
  .screen--menu{left:395px;top:30px;height:506px}
  .screen--categories{left:37px;top:569px;height:506px}
  .screen--questions{left:395px;top:569px;height:603px}
  .screen__photo{position:absolute;inset:0;
    background:
      radial-gradient(ellipse at 15% 80%, rgba(0,0,0,.55), transparent 45%),
      radial-gradient(ellipse at 60% 20%, rgba(70,90,110,.35), transparent 50%),
      linear-gradient(180deg,var(--photo-top) 0%,var(--photo-mid) 38%,var(--photo-low) 75%,var(--photo-base) 100%);}
  .screen__content{position:absolute;inset:0}
  .brand-mark{position:absolute;left:132px;width:54px;height:54px;border:2px solid var(--ink);border-radius:6px}
  .brand-name{position:absolute;left:0;right:0;text-align:center;font-weight:700;font-size:19.5px;letter-spacing:.2px;line-height:1;transform:translateY(-50%)}
  .tagline{position:absolute;left:20px;right:20px;top:276px;text-align:center;font-size:11.3px;font-weight:500;line-height:21px}
  .section-title{position:absolute;left:0;right:0;text-align:center;color:var(--accent);font-weight:700;font-size:15px;line-height:1;transform:translateY(-50%)}
  .section-sub{position:absolute;left:0;right:0;text-align:center;font-weight:500;font-size:12.5px;line-height:1;transform:translateY(-50%)}
  .back-link{position:absolute;left:8px;top:22px;font-size:11px;font-weight:500;display:flex;align-items:center;gap:6px}
  .count-tag{position:absolute;right:7px;font-size:11px;font-weight:600}
  .nav-button{position:absolute;left:9px;width:299px;height:47px;background:var(--panel);display:flex;align-items:center;justify-content:space-between;padding:0 13px;font-size:13px;font-weight:500}
  .arrow{width:12px;height:12px;flex:none}
  .view-all{position:absolute;left:112px;top:450px;width:92px;height:32px;background:var(--accent);color:var(--ink-dark);font-size:12px;font-weight:500;display:flex;align-items:center;justify-content:center}
  .question{position:absolute;left:9px;width:299px;background:var(--panel);display:flex;align-items:center;padding:0 13px 0 13px;font-size:10.5px;line-height:17.6px}
  .question__num{color:var(--accent);font-weight:600;font-style:italic;width:26px;flex:none;align-self:flex-start;padding-top:5px}
  .question__text{flex:1;padding-right:10px}
</style>
</head>
<body>

<svg width="0" height="0" style="position:absolute">
  <defs>
    <symbol id="arrow-circle" viewBox="0 0 12 12">
      <circle cx="6" cy="6" r="6" fill="#fff"/>
      <path d="M3 6h5M6 3.6 8.4 6 6 8.4" fill="none" stroke="#1562b0" stroke-width="1.5" stroke-linecap="round" stroke-linejoin="round"/>
    </symbol>
    <symbol id="chevron-left" viewBox="0 0 8 12">
      <path d="M6 1 1.5 6 6 11" fill="none" stroke="#fff" stroke-width="2" stroke-linecap="round" stroke-linejoin="round"/>
    </symbol>
  </defs>
</svg>

<!-- Splash -->
<section class="screen screen--splash">
  <div class="screen__photo" role="img" aria-label="Photo of a job interview in an office, tinted blue"></div>
  <div class="screen__content">
    <div class="brand-mark" style="top:171px"></div>
    <div class="brand-name" style="top:245px">LANTERN QUOKKA</div>
    <p class="tagline">Your guide to the most common interview questions, and the best responses to help you get hired.</p>
    <span class="count-tag" style="top:481px">x10</span>
  </div>
</section>

<!-- Menu -->
<section class="screen screen--menu">
  <div class="screen__photo" role="img" aria-label="Photo of a job interview in an office, tinted blue"></div>
  <div class="screen__content">
    <div class="brand-mark" style="top:23px"></div>
    <div class="brand-name" style="top:98px">LANTERN QUOKKA</div>
    <div class="section-title" style="top:159px">MENU</div>
    <div class="nav-button" style="top:180px">View Questions &amp; Responses<svg class="arrow"><use href="#arrow-circle"/></svg></div>
    <div class="nav-button" style="top:243px">My Question Portfolio<svg class="arrow"><use href="#arrow-circle"/></svg></div>
    <div class="nav-button" style="top:307px">Interview Tips<svg class="arrow"><use href="#arrow-circle"/></svg></div>
    <span class="count-tag" style="top:481px">x10</span>
  </div>
</section>

<!-- Categories -->
<section class="screen screen--categories">
  <div class="screen__photo" role="img" aria-label="Photo of a job interview in an office, tinted blue"></div>
  <div class="screen__content">
    <div class="back-link"><svg width="7" height="11"><use href="#chevron-left"/></svg>Back</div>
    <div class="brand-mark" style="top:23px"></div>
    <div class="brand-name" style="top:98px">LANTERN QUOKKA</div>
    <div class="section-title" style="top:149px">VIEW QUESTIONS &amp; RESPONSES</div>
    <div class="section-sub" style="top:172px">Select your question Category</div>
    <div class="nav-button" style="top:200px">Behavioral<svg class="arrow"><use href="#arrow-circle"/></svg></div>
    <div class="nav-button" style="top:264px">Situational<svg class="arrow"><use href="#arrow-circle"/></svg></div>
    <div class="nav-button" style="top:327px">Motivational<svg class="arrow"><use href="#arrow-circle"/></svg></div>
    <div class="nav-button" style="top:390px">Technical<svg class="arrow"><use href="#arrow-circle"/></svg></div>
    <div class="view-all">View All</div>
    <span class="count-tag" style="top:481px">x10</span>
  </div>
</section>

<!-- Questions list -->
<section class="screen screen--questions">
  <div class="screen__photo" role="img" aria-label="Photo of a job interview in an office, tinted blue"></div>
  <div class="screen__content">
    <div class="back-link"><svg width="7" height="11"><use href="#chevron-left"/></svg>Back</div>
    <div class="brand-mark" style="top:23px"></div>
    <div class="brand-name" style="top:98px">LANTERN QUOKKA</div>
    <div class="section-title" style="top:149px">VIEW QUESTIONS &amp; RESPONSES</div>
    <div class="section-sub" style="top:176px">Behavioral</div>
    <div class="question" style="top:200px;height:88px"><span class="question__num">1.</span><span class="question__text">Give me an example of a new idea or initiative you have suggested to your manager How did you implement this idea?</span><svg class="arrow"><use href="#arrow-circle"/></svg></div>
    <div class="question" style="top:299px;height:88px"><span class="question__num">2.</span><span class="question__text">Give me an example of a time when you made a mistake or didn't deliver on expectations, what happened? What did you learn?</span><svg class="arrow"><use href="#arrow-circle"/></svg></div>
    <div class="question" style="top:398px;height:49px"><span class="question__num">3.</span><span class="question__text">How would your colleagues describe you in three words?</span><svg class="arrow"><use href="#arrow-circle"/></svg></div>
    <div class="question" style="top:459px;height:49px"><span class="question__num">4.</span><span class="question__text">What parts of your current role frustrate you?</span><svg class="arrow"><use href="#arrow-circle"/></svg></div>
    <div class="question" style="top:520px;height:49px"><span class="question__num">5.</span><span class="question__text">What steps would you take to make an important decision on the job?</span><svg class="arrow"><use href="#arrow-circle"/></svg></div>
    <span class="count-tag" style="top:578px">x10</span>
  </div>
</section>

</body>
</html>
```